business card for a massage therapy practice named 'Meadow and Rowan Massage Studio'

I really need a trendy, yet easy on the eyes business card to complement my logo. Ideally with some gold or rose gold foil work.

My uploaded file of the logo I have in horizontal but I have a vertical version as well. Another color that is used in the website is a blush pink here and there. I'd like to see some trendy tropical leaves in the design.

```html
<!DOCTYPE html>
<html lang="en">
<head>
<meta charset="utf-8">
<title>Meadow &amp; Rowan Massage Studio — Business Card</title>
<link href="https://fonts.googleapis.com/css2?family=Montserrat:wght@400;500&family=Kaushan+Script&display=swap" rel="stylesheet">
<style>
  :root {
    --backdrop: #4b4d4c;
    --card: #1c1c1c;
    --copper: #c98a52;
    --copper-light: #dca06a;
    --copper-deep: #a8693a;
    --shadow: rgba(0, 0, 0, 0.45);
  }
  * { margin: 0; padding: 0; box-sizing: border-box; }
  html, body {
    width: 1198px;
    height: 1200px;
    overflow: hidden;
    background: var(--backdrop);
  }
  .canvas { position: relative; width: 1198px; height: 1200px; }

  .card {
    position: absolute;
    width: 698px;
    height: 397px;
    background: var(--card);
    box-shadow: -18px -14px 28px var(--shadow);
    overflow: hidden;
    color: var(--copper);
  }
  .card--front { left: 290px; top: 174px; }
  .card--back  { left: 291px; top: 693px; }

  /* Front: business name */
  .brand {
    position: absolute;
    left: 0; right: 0;
    top: 118px;
    text-align: center;
    font-family: "Montserrat", sans-serif;
    font-weight: 500;
    color: var(--copper);
  }
  .brand__name {
    font-size: 46px;
    letter-spacing: 2px;
    line-height: 1.2;
  }
  .brand__tag {
    margin-top: 14px;
    font-size: 26px;
    letter-spacing: 7px;
    text-transform: uppercase;
  }

  /* Back: decorative foliage areas */
  .foliage {
    position: absolute;
    background: linear-gradient(135deg, var(--copper-light), var(--copper-deep));
    opacity: 0.85;
  }
  .foliage--leaf-tl      { left: 0;   top: 0;   width: 84px;  height: 78px;  border-radius: 0 0 70px 0; }
  .foliage--fruit-top    { left: 164px; top: 0; width: 272px; height: 76px;  border-radius: 0 0 120px 120px; }
  .foliage--leaf-tr      { left: 484px; top: 0; width: 214px; height: 88px;  border-radius: 0 0 0 140px; }
  .foliage--leaf-left    { left: 0;   top: 185px; width: 100px; height: 207px; border-radius: 0 90px 40px 0; }
  .foliage--fruit-bottom { left: 207px; top: 328px; width: 256px; height: 69px; border-radius: 120px 120px 0 0; }
  .foliage--leaf-br      { left: 530px; top: 308px; width: 168px; height: 89px; border-radius: 120px 0 0 0; }

  /* Back: contact details */
  .contact {
    position: absolute;
    left: 0; right: 0;
    top: 112px;
    text-align: center;
    color: var(--copper);
  }
  .contact__name {
    font-family: "Kaushan Script", cursive;
    font-size: 37px;
    line-height: 1;
    margin-left: 40px;
  }
  .contact__list {
    list-style: none;
    margin-top: 26px;
    margin-left: 48px;
    font-family: "Montserrat", sans-serif;
    font-size: 16px;
    line-height: 24px;
    letter-spacing: 0.3px;
  }
  .contact__address {
    font-style: normal;
    margin-top: 14px;
    margin-left: 48px;
    font-family: "Montserrat", sans-serif;
    font-size: 16px;
    line-height: 24px;
    letter-spacing: 0.3px;
  }
</style>
</head>
<body>
<main class="canvas">

  <section class="card card--front" aria-label="Card front">
    <div class="brand">
      <div class="brand__name">Meadow &amp; Rowan</div>
      <div class="brand__tag">Massage Studio</div>
    </div>
  </section>

  <section class="card card--back" aria-label="Card back">
    <div class="foliage foliage--leaf-tl" role="img" aria-label="Copper foil palm leaf illustration"></div>
    <div class="foliage foliage--fruit-top" role="img" aria-label="Copper foil pineapple illustration"></div>
    <div class="foliage foliage--leaf-tr" role="img" aria-label="Copper foil palm frond illustration"></div>
    <div class="foliage foliage--leaf-left" role="img" aria-label="Copper foil palm leaf illustration"></div>
    <div class="foliage foliage--fruit-bottom" role="img" aria-label="Copper foil pineapple illustration"></div>
    <div class="foliage foliage--leaf-br" role="img" aria-label="Copper foil palm leaf illustration"></div>

    <div class="contact">
      <h1 class="contact__name">Elena Marsh</h1>
      <ul class="contact__list">
        <li>(555) 014-2278</li>
        <li>info@meadowandrowan.com</li>
        <li>www.meadowandrowan.com</li>
      </ul>
      <address class="contact__address">
        418 Linden Ave #210<br>
        Fairview, CA 95000
      </address>
    </div>
  </section>

</main>
</body>
</html>
```